Girls-Women's Athletic Clothing Line Needs Brochure

In need of a brochure for an athletic (Dance) apparel line called Morvel Apparel. The company makes athletic wear such as crops, leggings, shorts and pants such as those found in major retailers such as KeeKeeBrook Activa, Stridea by Fenn, Mira, Plucky Dora and a host of others. The unique perspective about Morvel is that we personalize all of our products with the name of the wearer.
The design, look and feel will draw inspiration from:
1) The colors used in the logo: Pink/Magenta and orange.
2) The stripe pattern used in the waistband and the product itself. See the website, www.morvelapparel.com for a greater understanding.
3) Athletics & Dance: Movement and energy
4) Our demographic is mainly mothers who buy for kids:
5) The design should represent happy and fun kids.
The Layout & Content must contain these items:
1) Purchase Procedure (found below). This is the procedure a customer goes through when buying a product on the site. I want the brochure to follow this pattern which highlights building your own unique garment.
2) An area for a description on the designer
"Purchase Procedure": (This will be worked into the layout & content of brochure)
1) PICK YOUR STYLE: the customer picks the desired style of bottom (pant, crop, legging, shorts).
2) CHOOSE YOUR COLOUR..customer then picks the desired color for the print (name and stripes).
3) WHAT'S YOUR NAME? ... customer then adds their desired name, nickname, initials, etc..
I have attached some stock images to use.
FURTHER:
Font for NAMES in the print is: Market Felt
Size of Brochure: US LETTER landscape: 11" x 8.5"
What is preferred file .jpg .psd. ai?
North American mothers.
Building

```html
<!DOCTYPE html>
<html lang="en">
<head>
<meta charset="utf-8">
<title>Morvel Apparel – Brochure Spread</title>
<link rel="stylesheet" href="https://fonts.googleapis.com/css2?family=Oswald:wght@300;400;600&family=Open+Sans:wght@400;600;700&display=swap">
<style>
  :root {
    --magenta: #d41c7e;
    --magenta-deep: #b5136a;
    --orange: #ec8b2e;
    --white: #ffffff;
    --paper-bg: #e9e9e9;
    --photo-light: #f1eeee;
    --photo-mid: #cfc6c9;
  }
  * { box-sizing: border-box; margin: 0; padding: 0; }
  html, body { width: 1200px; height: 800px; overflow: hidden; }
  body {
    background: var(--paper-bg);
    font-family: "Open Sans", Arial, sans-serif;
    position: relative;
  }
  .spread {
    position: absolute; left: 110px; top: 21px;
    width: 980px; height: 758px;
    display: flex;
    box-shadow: 0 6px 20px rgba(0,0,0,.18);
  }
  .panel { position: relative; width: 490px; height: 100%; overflow: hidden; background: var(--magenta); }
  .panel--inside { border-right: 1px solid rgba(0,0,0,.12); }

  /* Inside panel */
  .orange-band { position: absolute; left: 150px; top: 0; width: 340px; height: 100%; background: var(--orange); }
  .headline {
    position: absolute; left: 32px; top: 58px;
    font-family: "Oswald", "Arial Narrow", sans-serif; font-weight: 300;
    font-size: 54px; letter-spacing: 1px; color: var(--white); white-space: nowrap;
  }
  .feature-photo {
    position: absolute; width: 150px; height: 150px; border-radius: 50%;
    border: 9px solid var(--magenta-deep);
    background: radial-gradient(circle at 50% 45%, var(--photo-light) 40%, var(--photo-mid) 100%);
    box-shadow: 0 3px 8px rgba(0,0,0,.25);
  }
  .feature-photo--1 { left: 75px; top: 215px; }
  .feature-photo--2 { left: 75px; top: 385px; }
  .feature-photo--3 { left: 75px; top: 555px; }
  .feature-copy { position: absolute; left: 260px; width: 200px; }
  .feature-copy--1 { top: 205px; }
  .feature-copy--2 { top: 375px; }
  .feature-copy--3 { top: 545px; }
  .feature-heading {
    font-family: "Oswald", "Arial Narrow", sans-serif; font-weight: 600;
    font-size: 13px; letter-spacing: 1px; color: var(--magenta); text-align: right;
    margin-bottom: 10px;
  }
  .feature-text { font-size: 11.5px; line-height: 1.55; color: var(--white); }

  /* Cover panel */
  .edge-strip { position: absolute; right: 0; top: 0; width: 40px; height: 100%; background: var(--orange); }
  .contact { position: absolute; left: 28px; top: 36px; color: var(--white); }
  .contact-title {
    font-family: "Oswald", "Arial Narrow", sans-serif; font-weight: 400;
    font-size: 13px; letter-spacing: 1.5px; margin-bottom: 8px;
  }
  .contact-list { list-style: none; font-size: 10px; line-height: 1.8; }
  .contact-list li { display: flex; align-items: center; gap: 6px; }
  .contact-list svg { width: 10px; height: 10px; }
  .brand {
    position: absolute; right: 56px; top: 16px;
    display: flex; align-items: center; gap: 6px;
    font-family: "Oswald", "Arial Narrow", sans-serif; font-weight: 400;
    font-size: 22px; color: var(--white);
  }
  .brand-mark { width: 18px; height: 18px; background: var(--white); }
  .hero {
    position: absolute; left: 6px; top: 110px;
    width: 470px; height: 470px; border-radius: 50%;
    border: 12px solid var(--magenta-deep);
    box-shadow: 0 6px 16px rgba(0,0,0,.3);
    overflow: hidden; background: var(--white);
  }
  .hero-photo {
    position: absolute; inset: 0;
    background: radial-gradient(ellipse at 45% 45%, #e7dcdc 0%, #c7b7bb 45%, var(--white) 80%);
  }
  .hero-band {
    position: absolute; left: -60px; top: 250px; width: 600px; height: 110px;
    background: var(--magenta); opacity: .88; transform: rotate(-22deg);
  }
  .hero-callout {
    position: absolute; left: 125px; top: 262px; transform: rotate(-22deg);
    color: var(--white); text-align: center;
  }
  .callout-main { font-family: "Oswald", "Arial Narrow", sans-serif; font-weight: 400; font-size: 26px; line-height: 1.05; }
  .callout-sub { font-size: 10px; letter-spacing: 3px; font-weight: 600; margin-top: 4px; }
  .hero-tagline {
    position: absolute; left: 262px; top: 128px; transform: rotate(-22deg);
    font-family: "Oswald", "Arial Narrow", sans-serif; font-weight: 600;
    font-size: 25px; line-height: 1.05; letter-spacing: 1px; color: var(--white);
    text-align: center;
  }
</style>
</head>
<body>
  <main class="spread">
    <section class="panel panel--inside">
      <div class="orange-band"></div>
      <h1 class="headline">UNIQUE - LIKE YOU</h1>

      <div class="feature-photo feature-photo--1" role="img" aria-label="Photo of a girl in a dance pose wearing a crop top and shorts"></div>
      <div class="feature-copy feature-copy--1">
        <h2 class="feature-heading">HEADING 1</h2>
        <p class="feature-text">Pick your style: pants, crops, leggings or shorts, made to move with every dance.</p>
      </div>

      <div class="feature-photo feature-photo--2" role="img" aria-label="Photo of a girl stretching in athletic wear"></div>
      <div class="feature-copy feature-copy--2">
        <h2 class="feature-heading">HEADING 2</h2>
        <p class="feature-text">Choose your colour for the print, from bright stripes to soft tones she loves.</p>
      </div>

      <div class="feature-photo feature-photo--3" role="img" aria-label="Photo of a girl standing in leggings and a crop top"></div>
      <div class="feature-copy feature-copy--3">
        <h2 class="feature-heading">HEADING 3</h2>
        <p class="feature-text">Add her name, nickname or initials and make the piece truly her own.</p>
      </div>
    </section>

    <section class="panel panel--cover">
      <div class="edge-strip"></div>

      <div class="contact">
        <h2 class="contact-title">CONTACT US - 24/7</h2>
        <ul class="contact-list">
          <li><svg viewBox="0 0 10 10"><circle cx="5" cy="5" r="5" fill="#fff"/></svg>+1 555 010 2247</li>
          <li><svg viewBox="0 0 10 10"><circle cx="5" cy="5" r="5" fill="#fff"/></svg>hello@morvelapparel.com</li>
          <li><svg viewBox="0 0 10 10"><circle cx="5" cy="5" r="5" fill="#fff"/></svg>www.morvelapparel.com</li>
          <li><svg viewBox="0 0 10 10"><circle cx="5" cy="5" r="5" fill="#fff"/></svg>@morvelapparel</li>
        </ul>
      </div>

      <div class="brand"><span class="brand-mark"></span>Morvel</div>

      <div class="hero">
        <div class="hero-photo" role="img" aria-label="Group photo of smiling girls in matching crop tops and personalized leggings"></div>
        <div class="hero-band"></div>
        <div class="hero-callout">
          <p class="callout-main">Great for<br>Day Care!</p>
          <p class="callout-sub">MADE IN CANADA</p>
        </div>
        <p class="hero-tagline">PERSONALIZED<br>ACTIVE WEAR</p>
      </div>
    </section>
  </main>
</body>
</html>
```